Spice Mix Label Bottle Branding - Health and Weight Loss Mixes

The company is called ZestRow Spice Mix's. We've created 5 spice mixes using ingredients that promote health and weight loss. We already have a logo but now we need labels for our bottles. We would like to see designs that have the feel of health supplements (see attached examples)

We would like a different colour featured with each of our flavours.

Our flavours are:
-Golden Chai (Yellow)
-Mild Curry (Orange)
-Coffee Rub (brown)
-Garlic Oregano (Green)
-Taco (Blue)

Thank you!

Target Market(s)

Ages 22-35. Men and Female. Trendy, Hipster.

Industry/Entity Type

Food Production

Font styles to use
Sans Serif

Colors
f37122
0655a3
0692cd
9bcb3c
fbee3f

Requirements
Must have
• A different featured colour for each flavour.
• The ZestRow Spices Logo (attached)
• The slogan: "Weight Loss Ingredients"
• -Golden Chai (Yellow)
• -Mild Curry (Orange)
• -Coffee Rub (brown)
• -Garlic Oregano (Green)
• -Taco (Blue)
• Text Files attached.
Nice to have
• A black label with a featured colour for each of the spice mice flavours.
• 'No Salt added'

```html
<!DOCTYPE html>
<html lang="en">
<head>
<meta charset="utf-8">
<title>ZestRow Spices – Bottle Labels</title>
<link rel="stylesheet" href="https://fonts.googleapis.com/css2?family=Poppins:wght@300;400;500;600;700;800&family=Archivo+Narrow:wght@400;700&display=swap">
<style>
  :root {
    --page: #d5d6d8;
    --label-dark: #1d1d1e;
    --label-dark-2: #2a2a2b;
    --ink: #111111;
    --paper: #ffffff;
    --muted: #d8d8d8;
    --curry: #ef5a24;
    --chai: #d59f2a;
    --taco: #2f6aa6;
    --garlic: #8db83c;
    --coffee: #a4703c;
  }
  * { box-sizing: border-box; margin: 0; padding: 0; }
  html, body { width: 674px; height: 1200px; overflow: hidden; }
  body {
    background: var(--page);
    font-family: "Poppins", sans-serif;
    position: relative;
  }
  .label {
    position: absolute;
    left: 63px;
    width: 547px;
    height: 210px;
    background: linear-gradient(160deg, var(--label-dark-2), var(--label-dark) 55%);
    overflow: hidden;
    color: var(--paper);
  }
  .label--curry  { top: 54px;  --accent: var(--curry); }
  .label--chai   { top: 274px; --accent: var(--chai); }
  .label--taco   { top: 494px; --accent: var(--taco); }
  .label--garlic { top: 714px; --accent: var(--garlic); }
  .label--coffee { top: 934px; --accent: var(--coffee); }

  /* left column */
  .directions {
    position: absolute; left: 16px; top: 13px; width: 152px;
    font-size: 5.6px; line-height: 1.45; font-weight: 400;
  }
  .directions p { margin-bottom: 6px; }
  .directions .key { color: var(--accent); font-weight: 600; }
  .directions .warning { font-weight: 600; text-transform: uppercase; }
  .directions .contact { font-weight: 500; }
  .barcode-box {
    position: absolute; left: 22px; top: 154px; width: 138px; height: 46px;
    background: var(--accent);
    display: flex; align-items: center; justify-content: center;
    font-size: 15px; font-weight: 500; color: var(--paper);
  }
  .label--coffee .barcode-box { background: var(--paper); color: var(--coffee); }

  /* center column */
  .brand-panel { position: absolute; left: 182px; top: 0; width: 183px; height: 124px; }
  .brand-panel svg { position: absolute; inset: 0; }
  .brand-name {
    position: absolute; left: 0; right: 0; top: 44px;
    display: flex; align-items: center; justify-content: center; gap: 6px;
    font-size: 24px; font-weight: 800; color: var(--ink); letter-spacing: -0.5px;
  }
  .brand-mark { width: 10px; height: 10px; background: var(--accent); }
  .flavour {
    position: absolute; left: 196px; top: 126px;
    font-size: 16px; font-weight: 500; color: var(--accent); line-height: 1; letter-spacing: -0.2px;
  }
  .slogan {
    position: absolute; left: 196px; top: 143px;
    font-size: 10.5px; font-weight: 300; color: var(--paper); line-height: 1;
  }
  .claim {
    position: absolute; left: 196px; top: 158px; width: 128px;
    font-size: 4.4px; line-height: 1.35; color: var(--muted);
  }
  .supplement-tag {
    position: absolute; left: 196px; top: 186px;
    font-size: 7px; font-weight: 500; color: var(--accent);
  }
  .dose-tab {
    position: absolute; left: 313px; top: 182px; width: 38px; height: 18px;
    background: var(--paper); border-radius: 4px 4px 0 0;
    display: flex; align-items: center; justify-content: center;
    font-size: 7.5px; font-weight: 600; color: var(--accent);
  }
  .accent-band { position: absolute; left: 0; right: 0; top: 200px; height: 10px; background: var(--accent); }

  /* facts panel */
  .facts {
    position: absolute; left: 381px; top: 10px; width: 152px; height: 177px;
    background: var(--paper); color: var(--ink);
    padding: 4px;
    font-family: "Archivo Narrow", sans-serif;
  }
  .facts-frame { border: 1.5px solid var(--ink); height: 122px; padding: 2px 4px; font-size: 6px; line-height: 1.25; }
  .facts-title { font-family: "Poppins", sans-serif; font-weight: 700; font-size: 9.4px; letter-spacing: 0.2px; line-height: 1.1; }
  .rule-thick { border-top: 3px solid var(--ink); margin: 2px 0 1px; }
  .rule-thin { border-top: 0.6px solid var(--ink); }
  .row { display: flex; justify-content: space-between; padding: 1px 0; }
  .row .val { display: flex; gap: 10px; }
  .row .dv { width: 14px; text-align: right; }
  .row--head { font-weight: 700; justify-content: flex-end; gap: 14px; }
  .row--indent { padding-left: 7px; }
  .note { font-size: 5.8px; line-height: 1.2; margin-top: 1px; }
  .other { font-size: 6px; line-height: 1.2; margin-top: 3px; padding: 0 1px; }
</style>
</head>
<body>

<!-- one template repeated per flavour -->
<section class="label label--curry">
  <div class="directions">
    <p><span class="key">SUGGESTED USE:</span> Take 2 caplets by mouth daily.</p>
    <p><span class="key">CAUTIONS:</span> if you are under a physician's care or taking medication, consult you health care professional before using this product. if you are pregnant or nursing, do not use without consulting a physician.</p>
    <p class="warning">Keep out of reach of children. Do not use if safety seal is damaged or missing. Store in a cool, dry place.</p>
    <p class="contact">Distributed For:<br>Zestrowspices<br>support@zestrowspices</p>
  </div>
  <div class="barcode-box">Bar Code</div>
  <div class="brand-panel">
    <svg viewBox="0 0 183 124" width="183" height="124" aria-hidden="true"><path d="M0 0H183V116C150 104 115 126 78 120C48 115 22 106 0 112Z" fill="#fff"/></svg>
    <div class="brand-name"><span class="brand-mark"></span>ZestRow Spices</div>
  </div>
  <div class="flavour">MILD CURRY</div>
  <div class="slogan">INGREDIENTS</div>
  <p class="claim">Special Formulated with Garcinia Cambogia, Green Coffee, and Raspberry Ketone to support Metabolism and weight loss*</p>
  <div class="supplement-tag">Dietary Supplement</div>
  <div class="dose-tab">200mg</div>
  <div class="facts">
    <div class="facts-frame">
      <div class="facts-title">SUPPLEMENT FACTS</div>
      <div>Serving Size: 2 Softgels<br>Servings Per Container: 45</div>
      <div class="rule-thick"></div>
      <div class="row row--head"><span>Amount Per Serving</span><span>% DV</span></div>
      <div class="rule-thin"></div>
      <div class="row"><span>Calories</span><span class="val"><span>20</span><span class="dv"></span></span></div>
      <div class="rule-thin"></div>
      <div class="row row--indent"><span>Calories from Fat</span><span class="val"><span>20</span><span class="dv"></span></span></div>
      <div class="rule-thin"></div>
      <div class="row"><span>Total Fat</span><span class="val"><span>2g</span><span class="dv">3%**</span></span></div>
      <div class="rule-thin"></div>
      <div class="row"><span>CLA (Conjugated Linoleic&nbsp;&nbsp;1600 mg<br>Acid)(from Safflower Oil)</span><span>†</span></div>
      <div class="rule-thick"></div>
      <div class="note">**Percent Daily Values (% DV) are based on a 2,000 calorie diet.<br>† Daily Value not established.</div>
    </div>
    <div class="other">Other Ingredients: Gelatin, Glycerin, Purified Water, Caramel.</div>
  </div>
  <div class="accent-band"></div>
</section>

<section class="label label--chai">
  <div class="directions">
    <p><span class="key">SUGGESTED USE:</span> Take 2 caplets by mouth daily.</p>
    <p><span class="key">CAUTIONS:</span> if you are under a physician's care or taking medication, consult you health care professional before using this product. if you are pregnant or nursing, do not use without consulting a physician.</p>
    <p class="warning">Keep out of reach of children. Do not use if safety seal is damaged or missing. Store in a cool, dry place.</p>
    <p class="contact">Distributed For:<br>Zestrowspices<br>support@zestrowspices</p>
  </div>
  <div class="barcode-box">Bar Code</div>
  <div class="brand-panel">
    <svg viewBox="0 0 183 124" width="183" height="124" aria-hidden="true"><path d="M0 0H183V116C150 104 115 126 78 120C48 115 22 106 0 112Z" fill="#fff"/></svg>
    <div class="brand-name"><span class="brand-mark"></span>ZestRow Spices</div>
  </div>
  <div class="flavour">GOLDEN CHAI</div>
  <div class="slogan">INGREDIENTS</div>
  <p class="claim">Special Formulated with Garcinia Cambogia, Green Coffee, and Raspberry Ketone to support Metabolism and weight loss*</p>
  <div class="supplement-tag">Dietary Supplement</div>
  <div class="dose-tab">200mg</div>
  <div class="facts">
    <div class="facts-frame">
      <div class="facts-title">SUPPLEMENT FACTS</div>
      <div>Serving Size: 2 Softgels<br>Servings Per Container: 45</div>
      <div class="rule-thick"></div>
      <div class="row row--head"><span>Amount Per Serving</span><span>% DV</span></div>
      <div class="rule-thin"></div>
      <div class="row"><span>Calories</span><span class="val"><span>20</span><span class="dv"></span></span></div>
      <div class="rule-thin"></div>
      <div class="row row--indent"><span>Calories from Fat</span><span class="val"><span>20</span><span class="dv"></span></span></div>
      <div class="rule-thin"></div>
      <div class="row"><span>Total Fat</span><span class="val"><span>2g</span><span class="dv">3%**</span></span></div>
      <div class="rule-thin"></div>
      <div class="row"><span>CLA (Conjugated Linoleic&nbsp;&nbsp;1600 mg<br>Acid)(from Safflower Oil)</span><span>†</span></div>
      <div class="rule-thick"></div>
      <div class="note">**Percent Daily Values (% DV) are based on a 2,000 calorie diet.<br>† Daily Value not established.</div>
    </div>
    <div class="other">Other Ingredients: Gelatin, Glycerin, Purified Water, Caramel.</div>
  </div>
  <div class="accent-band"></div>
</section>

<section class="label label--taco">
  <div class="directions">
    <p><span class="key">SUGGESTED USE:</span> Take 2 caplets by mouth daily.</p>
    <p><span class="key">CAUTIONS:</span> if you are under a physician's care or taking medication, consult you health care professional before using this product. if you are pregnant or nursing, do not use without consulting a physician.</p>
    <p class="warning">Keep out of reach of children. Do not use if safety seal is damaged or missing. Store in a cool, dry place.</p>
    <p class="contact">Distributed For:<br>Zestrowspices<br>support@zestrowspices</p>
  </div>
  <div class="barcode-box">Bar Code</div>
  <div class="brand-panel">
    <svg viewBox="0 0 183 124" width="183" height="124" aria-hidden="true"><path d="M0 0H183V116C150 104 115 126 78 120C48 115 22 106 0 112Z" fill="#fff"/></svg>
    <div class="brand-name"><span class="brand-mark"></span>ZestRow Spices</div>
  </div>
  <div class="flavour">TACO</div>
  <div class="slogan">INGREDIENTS</div>
  <p class="claim">Special Formulated with Garcinia Cambogia, Green Coffee, and Raspberry Ketone to support Metabolism and weight loss*</p>
  <div class="supplement-tag">Dietary Supplement</div>
  <div class="dose-tab">200mg</div>
  <div class="facts">
    <div class="facts-frame">
      <div class="facts-title">SUPPLEMENT FACTS</div>
      <div>Serving Size: 2 Softgels<br>Servings Per Container: 45</div>
      <div class="rule-thick"></div>
      <div class="row row--head"><span>Amount Per Serving</span><span>% DV</span></div>
      <div class="rule-thin"></div>
      <div class="row"><span>Calories</span><span class="val"><span>20</span><span class="dv"></span></span></div>
      <div class="rule-thin"></div>
      <div class="row row--indent"><span>Calories from Fat</span><span class="val"><span>20</span><span class="dv"></span></span></div>
      <div class="rule-thin"></div>
      <div class="row"><span>Total Fat</span><span class="val"><span>2g</span><span class="dv">3%**</span></span></div>
      <div class="rule-thin"></div>
      <div class="row"><span>CLA (Conjugated Linoleic&nbsp;&nbsp;1600 mg<br>Acid)(from Safflower Oil)</span><span>†</span></div>
      <div class="rule-thick"></div>
      <div class="note">**Percent Daily Values (% DV) are based on a 2,000 calorie diet.<br>† Daily Value not established.</div>
    </div>
    <div class="other">Other Ingredients: Gelatin, Glycerin, Purified Water, Caramel.</div>
  </div>
  <div class="accent-band"></div>
</section>

<section class="label label--garlic">
  <div class="directions">
    <p><span class="key">SUGGESTED USE:</span> Take 2 caplets by mouth daily.</p>
    <p><span class="key">CAUTIONS:</span> if you are under a physician's care or taking medication, consult you health care professional before using this product. if you are pregnant or nursing, do not use without consulting a physician.</p>
    <p class="warning">Keep out of reach of children. Do not use if safety seal is damaged or missing. Store in a cool, dry place.</p>
    <p class="contact">Distributed For:<br>Zestrowspices<br>support@zestrowspices</p>
  </div>
  <div class="barcode-box">Bar Code</div>
  <div class="brand-panel">
    <svg viewBox="0 0 183 124" width="183" height="124" aria-hidden="true"><path d="M0 0H183V116C150 104 115 126 78 120C48 115 22 106 0 112Z" fill="#fff"/></svg>
    <div class="brand-name"><span class="brand-mark"></span>ZestRow Spices</div>
  </div>
  <div class="flavour">GARLIC OREGANO</div>
  <div class="slogan">INGREDIENTS</div>
  <p class="claim">Special Formulated with Garcinia Cambogia, Green Coffee, and Raspberry Ketone to support Metabolism and weight loss*</p>
  <div class="supplement-tag">Dietary Supplement</div>
  <div class="dose-tab">200mg</div>
  <div class="facts">
    <div class="facts-frame">
      <div class="facts-title">SUPPLEMENT FACTS</div>
      <div>Serving Size: 2 Softgels<br>Servings Per Container: 45</div>
      <div class="rule-thick"></div>
      <div class="row row--head"><span>Amount Per Serving</span><span>% DV</span></div>
      <div class="rule-thin"></div>
      <div class="row"><span>Calories</span><span class="val"><span>20</span><span class="dv"></span></span></div>
      <div class="rule-thin"></div>
      <div class="row row--indent"><span>Calories from Fat</span><span class="val"><span>20</span><span class="dv"></span></span></div>
      <div class="rule-thin"></div>
      <div class="row"><span>Total Fat</span><span class="val"><span>2g</span><span class="dv">3%**</span></span></div>
      <div class="rule-thin"></div>
      <div class="row"><span>CLA (Conjugated Linoleic&nbsp;&nbsp;1600 mg<br>Acid)(from Safflower Oil)</span><span>†</span></div>
      <div class="rule-thick"></div>
      <div class="note">**Percent Daily Values (% DV) are based on a 2,000 calorie diet.<br>† Daily Value not established.</div>
    </div>
    <div class="other">Other Ingredients: Gelatin, Glycerin, Purified Water, Caramel.</div>
  </div>
  <div class="accent-band"></div>
</section>

<section class="label label--coffee">
  <div class="directions">
    <p><span class="key">SUGGESTED USE:</span> Take 2 caplets by mouth daily.</p>
    <p><span class="key">CAUTIONS:</span> if you are under a physician's care or taking medication, consult you health care professional before using this product. if you are pregnant or nursing, do not use without consulting a physician.</p>
    <p class="warning">Keep out of reach of children. Do not use if safety seal is damaged or missing. Store in a cool, dry place.</p>
    <p class="contact">Distributed For:<br>Zestrowspices<br>support@zestrowspices</p>
  </div>
  <div class="barcode-box">Bar Code</div>
  <div class="brand-panel">
    <svg viewBox="0 0 183 124" width="183" height="124" aria-hidden="true"><path d="M0 0H183V116C150 104 115 126 78 120C48 115 22 106 0 112Z" fill="#fff"/></svg>
    <div class="brand-name"><span class="brand-mark"></span>ZestRow Spices</div>
  </div>
  <div class="flavour">COFFEE RUB</div>
  <div class="slogan">INGREDIENTS</div>
  <p class="claim">Special Formulated with Garcinia Cambogia, Green Coffee, and Raspberry Ketone to support Metabolism and weight loss*</p>
  <div class="supplement-tag">Dietary Supplement</div>
  <div class="dose-tab">200mg</div>
  <div class="facts">
    <div class="facts-frame">
      <div class="facts-title">SUPPLEMENT FACTS</div>
      <div>Serving Size: 2 Softgels<br>Servings Per Container: 45</div>
      <div class="rule-thick"></div>
      <div class="row row--head"><span>Amount Per Serving</span><span>% DV</span></div>
      <div class="rule-thin"></div>
      <div class="row"><span>Calories</span><span class="val"><span>20</span><span class="dv"></span></span></div>
      <div class="rule-thin"></div>
      <div class="row row--indent"><span>Calories from Fat</span><span class="val"><span>20</span><span class="dv"></span></span></div>
      <div class="rule-thin"></div>
      <div class="row"><span>Total Fat</span><span class="val"><span>2g</span><span class="dv">3%**</span></span></div>
      <div class="rule-thin"></div>
      <div class="row"><span>CLA (Conjugated Linoleic&nbsp;&nbsp;1600 mg<br>Acid)(from Safflower Oil)</span><span>†</span></div>
      <div class="rule-thick"></div>
      <div class="note">**Percent Daily Values (% DV) are based on a 2,000 calorie diet.<br>† Daily Value not established.</div>
    </div>
    <div class="other">Other Ingredients: Gelatin, Glycerin, Purified Water, Caramel.</div>
  </div>
  <div class="accent-band"></div>
</section>

</body>
</html>
```